Bright Path Attorneys Billboard Design for Personal Injury Law Firm

Need a billboard design that we can use for different versions. 1400px X 400px jpeg or png
I have attached the logo and the attorney for the billboard. Attorney Marla Benning
Here is a link to our current website brightpathlegalgroup.example

HEADLINE: HIT BY A TRUCK?
SUBHEAD: NO FEE. BIG FIGHT.
877-GRANTLY

HEADLINE: ACCIDENT?
SUBHEAD: NO FEE, UNLESS WE WIN!
877-GRANTLY

HEADLINE: BIG TRUCK. BIG CASE.
SUBHEAD: YOU PAY $0 UPFRONT
877-GRANTLY

Target Market(s)

People in Car Accident

Industry/Entity Type

Personal Injury Attorneys

```html
<!DOCTYPE html>
<html lang="en">
<head>
<meta charset="utf-8">
<title>Bright Path Attorneys – Billboard Set</title>
<link href="https://fonts.googleapis.com/css2?family=Montserrat:wght@500;600;700;800;900&display=swap" rel="stylesheet">
<style>
  :root {
    --page: #ffffff;
    --navy-top: #070a2e;
    --navy-bottom: #0b4a74;
    --yellow: #ffc907;
    --white: #ffffff;
    --black: #000000;
    --photo-sky: #d9823a;
    --photo-dusk: #3b2a2a;
    --photo-dark: #15151c;
  }
  * { margin: 0; padding: 0; box-sizing: border-box; }
  html, body {
    width: 1200px; height: 1084px; overflow: hidden;
    background: var(--page);
    font-family: "Montserrat", Arial, sans-serif;
  }
  .board-set { position: relative; width: 1200px; height: 1084px; }
  .billboard {
    position: absolute; left: 21px; width: 1158px; height: 332px;
    overflow: hidden;
    background: linear-gradient(180deg, var(--navy-top) 0%, var(--navy-bottom) 100%);
  }
  .billboard--truck { top: 25px; }
  .billboard--accident { top: 379px; }
  .billboard--case { top: 732px; }
  .billboard__art { position: absolute; inset: 0; width: 100%; height: 100%; }
  .copy { position: absolute; font-weight: 800; line-height: 1; white-space: nowrap; letter-spacing: -0.5px; }
  .copy--headline { color: var(--yellow); font-weight: 900; }
  .copy--sub { color: var(--white); font-weight: 700; letter-spacing: 0; }
  .copy--phone { color: var(--white); font-weight: 900; }
  .align-right { right: 45px; text-align: right; }
  .align-left { left: 45px; }

  .brand {
    position: absolute; display: flex; align-items: center; gap: 9px;
    color: var(--white); font-weight: 700; line-height: 1;
  }
  .brand__dot { width: 30px; height: 30px; border-radius: 50%; background: var(--white); flex: none; }
  .brand__name { display: flex; flex-direction: column; gap: 3px; }
  .brand__main { font-size: 22px; letter-spacing: 0.3px; }
  .brand__sub { font-size: 10px; letter-spacing: 4.6px; }

  /* Truck */
  .billboard--truck .brand { top: 30px; right: 30px; }
  .billboard--truck .copy--headline { top: 106px; font-size: 80px; }
  .billboard--truck .copy--sub { top: 193px; font-size: 44px; }
  .billboard--truck .copy--phone { top: 244px; font-size: 70px; }

  /* Accident */
  .billboard--accident .brand { top: 26px; left: 45px; }
  .billboard--accident .copy--headline { top: 92px; font-size: 104px; }
  .billboard--accident .copy--sub { top: 196px; font-size: 45px; }
  .billboard--accident .copy--phone { top: 246px; font-size: 70px; }

  /* Big case */
  .billboard--case .brand { bottom: 28px; left: 36px; }
  .billboard--case .copy--headline { font-size: 82px; }
  .billboard--case .align-right { right: 30px; }
  .billboard--case .headline-line-1 { top: 24px; right: 130px; }
  .billboard--case .headline-line-2 { top: 102px; }
  .billboard--case .copy--sub { top: 190px; font-size: 45px; }
  .billboard--case .copy--phone { top: 238px; font-size: 70px; }
</style>
</head>
<body>
<main class="board-set">

  <section class="billboard billboard--truck">
    <svg class="billboard__art" viewBox="0 0 1400 400" preserveAspectRatio="none">
      <defs>
        <linearGradient id="truckPhotoA" x1="0" y1="0" x2="1" y2="1">
          <stop offset="0" stop-color="var(--photo-sky)"/>
          <stop offset="0.45" stop-color="var(--photo-dusk)"/>
          <stop offset="1" stop-color="var(--photo-dark)"/>
        </linearGradient>
      </defs>
      <polygon points="210,0 470,0 560,200 470,400 300,400 460,255" fill="var(--black)"/>
      <polygon points="0,0 205,0 470,260 300,400 0,400" fill="var(--white)"/>
      <polygon role="img" aria-label="Photo of a semi truck driving on a desert highway at sunset"
               points="0,0 190,0 445,260 285,400 0,400" fill="url(#truckPhotoA)"/>
    </svg>
    <div class="brand"><span class="brand__dot"></span><span class="brand__name"><span class="brand__main">BRIGHT PATH</span><span class="brand__sub">ATTORNEYS</span></span></div>
    <h2 class="copy copy--headline align-right">HIT BY A TRUCK</h2>
    <p class="copy copy--sub align-right">NO FEE. BIG FIGHT.</p>
    <p class="copy copy--phone align-right">877-GRANTLY</p>
  </section>

  <section class="billboard billboard--accident">
    <svg class="billboard__art" viewBox="0 0 1400 400" preserveAspectRatio="none">
      <defs>
        <linearGradient id="truckPhotoB" x1="0" y1="0" x2="1" y2="1">
          <stop offset="0" stop-color="var(--photo-dark)"/>
          <stop offset="0.5" stop-color="var(--photo-sky)"/>
          <stop offset="1" stop-color="var(--photo-dusk)"/>
        </linearGradient>
      </defs>
      <polygon points="870,0 1400,0 1400,400 1080,400" fill="var(--black)"/>
      <polygon points="915,0 1400,0 1400,245 1135,400" fill="var(--white)"/>
      <polygon role="img" aria-label="Close photo of a truck cab reflecting the sunset"
               points="935,0 1400,0 1400,262 1150,385" fill="url(#truckPhotoB)"/>
    </svg>
    <div class="brand"><span class="brand__dot"></span><span class="brand__name"><span class="brand__main">BRIGHT PATH</span><span class="brand__sub">ATTORNEYS</span></span></div>
    <h2 class="copy copy--headline align-left">ACCIDENT</h2>
    <p class="copy copy--sub align-left">NO FEE, UNLESS WE WIN!</p>
    <p class="copy copy--phone align-left">877-GRANTLY</p>
  </section>

  <section class="billboard billboard--case">
    <svg class="billboard__art" viewBox="0 0 1400 400" preserveAspectRatio="none">
      <defs>
        <linearGradient id="truckPhotoC" x1="0" y1="0" x2="1" y2="1">
          <stop offset="0" stop-color="var(--photo-dark)"/>
          <stop offset="0.55" stop-color="var(--photo-dusk)"/>
          <stop offset="1" stop-color="var(--photo-sky)"/>
        </linearGradient>
      </defs>
      <polygon points="210,0 470,0 560,200 470,400 300,400 460,255" fill="var(--black)"/>
      <polygon points="0,0 205,0 470,260 300,400 0,400" fill="var(--white)"/>
      <polygon role="img" aria-label="Photo of a semi truck front on the highway at sunset"
               points="0,0 190,0 445,260 285,400 0,400" fill="url(#truckPhotoC)"/>
    </svg>
    <div class="brand"><span class="brand__dot"></span><span class="brand__name"><span class="brand__main">BRIGHT PATH</span><span class="brand__sub">ATTORNEYS</span></span></div>
    <h2 class="copy copy--headline align-right headline-line-1">BIG TRUCK.</h2>
    <h2 class="copy copy--headline align-right headline-line-2">BIG CASE.</h2>
    <p class="copy copy--sub align-right">YOU PAY $0 UPFRONT</p>
    <p class="copy copy--phone align-right">877-GRANTLY</p>
  </section>

</main>
</body>
</html>
```